Visitenkarten-Design für Maler
Zielgruppe
Ausführung von Malerarbeiten,Innenraumgestaltung
Aufgabenstellung
Stichworte :Eilaufträge Seniorenservice Kleinaufträge

```html
<!DOCTYPE html>
<html lang="de">
<head>
<meta charset="utf-8">
<title>Visitenkarte Malerfachbetrieb Jonas Feldberg</title>
<link href="https://fonts.googleapis.com/css2?family=Lato:wght@400;700&display=swap" rel="stylesheet">
<style>
  :root {
    --bg: #eeeeee;
    --card: #fbfbfb;
    --blue: #069fe0;
    --red: #e01f2b;
    --yellow: #fbcd12;
    --green: #43ad56;
    --text: #4e4e4e;
    --text-soft: #5c5c5c;
  }
  * { margin: 0; padding: 0; box-sizing: border-box; }
  html, body {
    width: 1200px;
    height: 864px;
    overflow: hidden;
    background: var(--bg);
    font-family: "Lato", sans-serif;
  }
  .canvas {
    position: relative;
    width: 1200px;
    height: 864px;
    display: flex;
    justify-content: center;
    align-items: center;
    gap: 70px;
  }
  .card {
    position: relative;
    width: 330px;
    height: 510px;
    background: var(--card);
    box-shadow: 0 10px 28px rgba(0,0,0,0.12);
    overflow: hidden;
  }

  /* Front */
  .front__band {
    height: 112px;
    background: var(--blue);
  }
  .brand {
    position: absolute;
    top: 190px;
    left: 0;
    right: 0;
    display: flex;
    justify-content: center;
    align-items: center;
    gap: 12px;
  }
  .brand__dot {
    width: 34px;
    height: 34px;
    border-radius: 50%;
    background: var(--blue);
  }
  .brand__name {
    font-weight: 700;
    font-size: 17px;
    line-height: 1.15;
    color: var(--text-soft);
  }
  .services {
    position: absolute;
    top: 350px;
    left: 0;
    right: 0;
    text-align: center;
    color: var(--text);
  }
  .services__list {
    font-weight: 700;
    font-size: 12.5px;
    letter-spacing: 0.1px;
  }
  .services__mobile {
    margin-top: 8px;
    font-weight: 400;
    font-size: 13px;
    color: var(--text-soft);
  }

  /* Back */
  .back__band { height: 104px; }
  .back__band + .back__band { border-top: 3px solid var(--card); }
  .back__band--red { background: var(--red); }
  .back__band--yellow { background: var(--yellow); height: 107px; }
  .back__band--green { background: var(--green); height: 107px; }
  .contact {
    position: absolute;
    left: 34px;
    bottom: 56px;
    list-style: none;
    font-size: 11.5px;
    line-height: 1.85;
    color: var(--text-soft);
  }
</style>
</head>
<body>
<main class="canvas">
  <section class="card card--front">
    <div class="front__band"></div>
    <div class="brand">
      <span class="brand__dot"></span>
      <p class="brand__name">Malerfachbetrieb<br>Jonas Feldberg</p>
    </div>
    <div class="services">
      <p class="services__list">Eilaufträge / Seniorenservice / Kleinaufträge</p>
      <p class="services__mobile">Mobil: 0160/73518246</p>
    </div>
  </section>

  <section class="card card--back">
    <div class="back__band back__band--red"></div>
    <div class="back__band back__band--yellow"></div>
    <div class="back__band back__band--green"></div>
    <ul class="contact">
      <li>Tel. 030/48217703</li>
      <li>www.malerbetrieb-jonas-feldberg.de</li>
      <li>E-Mail: info@malerbetrieb-jonas-feldberg.de</li>
    </ul>
  </section>
</main>
</body>
</html>
```